Simple, bright, clean website - 3 pages, easy to update with WordPress!

I want to update my website (brelvatix.com) with a brighter/cleaner interface. It is quite dark right now. I would like it to be similar to a partner site (https://www.nodavent-44.com/). White with some orange highlights (matching the logo). I want to be able to easily update the site content. There should be 3 main pages: About, Services, Contact. I also like a design similar to quorfen.com

Target Market(s)

Anyone using technology to achieve business goals.

Industry/Entity Type

Managed Service Provider (IT)

Coding

Coded - Design and coding required

Number of Pages Required

3 page

Colors
F0912C
F2A743
F7CA91
FBE8D2
FDF5EE

Requirements
Must have
• Links to standard social media apps like WorkLattice, Pallgrove, etc.. Easy to edit and add pages.

```html
<!DOCTYPE html>
<html lang="en">
<head>
<meta charset="utf-8">
<title>Brelvatix – Managed IT Services</title>
<link href="https://fonts.googleapis.com/css2?family=Poppins:wght@300;400;500;600;700&display=swap" rel="stylesheet">
<style>
:root{
  --orange:#F5A614;
  --orange-deep:#F0912C;
  --orange-mid:#F2A743;
  --peach:#F7CA91;
  --sand:#FBE8D2;
  --cream:#FDF5EE;
  --white:#ffffff;
  --ink:#222222;
  --text:#444444;
  --muted:#9a9a9a;
  --grey-btn:#4a4a4a;
  --footer-dark:#555555;
}
*{margin:0;padding:0;box-sizing:border-box}
html,body{width:1200px;height:4173px;overflow:hidden}
body{font-family:"Poppins",sans-serif;color:var(--text);background:var(--white);position:relative}
.abs{position:absolute}
a{color:inherit;text-decoration:none}

/* header */
.site-header{position:absolute;left:0;top:0;width:1200px;height:138px;background:var(--white)}
.brand{position:absolute;left:86px;top:36px;font-family:"Poppins",sans-serif;font-weight:300;font-size:56px;color:#7a7a7a;letter-spacing:1px;line-height:70px}
.top-btn{position:absolute;top:34px;height:39px;border-radius:20px;color:#fff;font-size:13px;font-weight:600;display:flex;align-items:center;justify-content:center;gap:8px;text-transform:uppercase}
.btn-login{left:717px;width:178px;background:var(--grey-btn)}
.btn-connect{left:907px;width:207px;background:var(--orange)}
.main-nav{position:absolute;top:90px;left:0;width:1200px;font-size:14px;color:#333}
.main-nav a{position:absolute;text-transform:uppercase;white-space:nowrap}
.main-nav a.active{color:var(--orange)}
.main-nav a.active::after{content:"";position:absolute;left:-8px;right:-8px;top:26px;height:2px;background:var(--orange)}

/* hero */
.hero{position:absolute;left:0;top:138px;width:1200px;height:721px;background:linear-gradient(180deg,#6b5c4e 0%,#8a7562 40%,#7a6a5c 70%,#9b8a78 100%)}
.hero-tag{position:absolute;top:104px;width:100%;text-align:center;font-size:38px;color:var(--orange);font-weight:400}
.hero-line1{position:absolute;top:148px;width:100%;text-align:center;font-size:70px;font-weight:700;color:#fff;line-height:84px}
.hero-band{position:absolute;left:213px;top:212px;width:792px;height:97px;background:rgba(40,35,30,.55)}
.hero-line2{position:absolute;top:220px;width:100%;text-align:center;font-size:70px;font-weight:700;color:#fff;line-height:84px}
.hero-cta{position:absolute;left:491px;top:322px;width:219px;height:62px;border-radius:31px;background:var(--orange);color:#fff;font-size:18px;font-weight:600;display:flex;align-items:center;justify-content:center}
.dots{position:absolute;top:643px;left:562px;display:flex;gap:6px}
.dots span{width:14px;height:14px;border-radius:50%;background:rgba(255,255,255,.55)}
.dots span.on{background:#fff}

/* section heads */
.sec-title{position:absolute;width:100%;text-align:center;font-size:48px;font-weight:500;color:var(--orange);line-height:56px}
.sec-sub{position:absolute;font-size:24px;color:#999;letter-spacing:4px;font-weight:300}

/* about */
.about{position:absolute;left:0;top:859px;width:1200px;height:670px;background:var(--cream)}
.about-frame{position:absolute;left:135px;top:101px;width:422px;height:466px;background:var(--orange)}
.about-photo{position:absolute;left:157px;top:120px;width:421px;height:467px;background:linear-gradient(135deg,#c9a884,#e6d2b8 50%,#a98a6c)}
.about-line{position:absolute;left:157px;top:109px;width:400px;height:458px;border:1px solid #fff}
.about-title{position:absolute;left:643px;top:152px;font-size:44px;font-weight:500;color:var(--orange);line-height:52px}
.about-sub{position:absolute;left:680px;top:200px;font-size:21px;color:#999;letter-spacing:3px;font-weight:300}
.about-text{position:absolute;left:643px;top:252px;width:422px;font-size:15px;line-height:31px;color:#444;text-align:justify}
.pill{position:absolute;border-radius:30px;background:var(--orange);color:#fff;font-weight:500;display:flex;align-items:center;justify-content:center;text-transform:uppercase}

/* services */
.services{position:absolute;left:0;top:1529px;width:1200px;height:971px;background:var(--white)}
.services-intro{position:absolute;left:150px;top:208px;width:900px;text-align:center;font-size:15px;line-height:31px;color:#444}
.svc-img{position:absolute;width:316px;height:232px}
.svc-label{position:absolute;width:265px;height:69px;background:#fff;box-shadow:0 3px 8px rgba(0,0,0,.12);display:flex;align-items:center;justify-content:center;font-size:16px;font-weight:500;color:#222}
.svc-label.hot{background:var(--orange);color:#fff}
.circle-btn{position:absolute;width:48px;height:48px;border-radius:50%;display:flex;align-items:center;justify-content:center}
.circle-btn.grey{background:#8a8a8a}
.circle-btn.orange{background:var(--orange)}

/* testimonials */
.testimonials{position:absolute;left:0;top:2500px;width:1200px;height:562px;background:var(--cream)}
.t-avatar{position:absolute;width:90px;height:90px;border-radius:50%;background:linear-gradient(160deg,#d9c4ae,#8c7a68)}
.t-quote{position:absolute;width:215px;font-size:11.5px;line-height:19.5px;color:#444;text-align:justify}
.t-quote b{color:var(--orange);font-size:20px;font-weight:700;margin-right:10px;line-height:10px}
.t-name{position:absolute;font-size:14px;font-weight:500;color:#222}
.t-stars{position:absolute;font-size:10px;color:var(--orange);letter-spacing:1px}

/* contact */
.contact{position:absolute;left:0;top:3062px;width:1200px;height:606px;background:var(--white)}
.orange-band{position:absolute;left:0;top:3668px;width:1200px;height:435px;background:var(--orange)}
.contact-box{position:absolute;left:220px;top:3280px;width:763px;height:542px;background:var(--cream)}
.contact-bar{position:absolute;left:12px;top:6px;width:740px;height:7px;background:var(--orange)}
.field{position:absolute;left:52px;width:332px;background:#fff;box-shadow:0 2px 6px rgba(0,0,0,.1);font-size:15px;color:#999;padding:18px 24px}
.info-ico{position:absolute;left:428px;width:34px;height:34px;border-radius:5px;background:var(--orange);display:flex;align-items:center;justify-content:center}
.info-head{position:absolute;left:488px;font-size:18px;color:var(--orange);text-transform:uppercase}
.info-text{position:absolute;left:488px;font-size:17px;color:#222;line-height:20px}

/* footer */
.footer-brand{position:absolute;top:3862px;width:100%;text-align:center;font-weight:300;font-size:92px;color:#fff;line-height:110px;letter-spacing:2px}
.footer-rule{position:absolute;left:89px;top:4018px;width:1030px;height:1px;background:rgba(255,255,255,.6)}
.footer-nav{position:absolute;top:4042px;left:0;width:1200px;color:#fff;font-size:15px}
.footer-nav span{position:absolute;white-space:nowrap}
.legal{position:absolute;left:0;top:4103px;width:1200px;height:70px;background:var(--footer-dark)}
.legal p{position:absolute;left:89px;top:24px;font-size:14px;color:#fff}
.social{position:absolute;top:17px;width:35px;height:35px;border:1.5px solid #fff;border-radius:3px}
</style>
</head>
<body>

<header class="site-header">
  <div class="brand">brelvatix</div>
  <a class="top-btn btn-login" href="#">
    <svg width="14" height="15" viewBox="0 0 14 15"><circle cx="7" cy="4" r="3.5" fill="#fff"/><path d="M0 15c0-4 3-6 7-6s7 2 7 6z" fill="#fff"/></svg>
    Client Login
  </a>
  <a class="top-btn btn-connect" href="#">
    <svg width="18" height="18" viewBox="0 0 18 18" fill="none" stroke="#fff" stroke-width="2"><path d="M7 11l4-4"/><path d="M8 5l2-2a3 3 0 014 4l-2 2"/><path d="M10 13l-2 2a3 3 0 01-4-4l2-2"/></svg>
    Connect My Tech
  </a>
  <nav class="main-nav">
    <a class="active" href="#" style="left:710px">Home</a>
    <a href="#" style="left:791px">About Us</a>
    <a href="#" style="left:906px">Services</a>
    <a href="#" style="left:1017px">Contact Us</a>
  </nav>
</header>

<section class="hero" role="img" aria-label="Photo of a team meeting around a long conference table with laptops">
  <div class="hero-tag">Brelvatix</div>
  <div class="hero-line1">WE PROVIDE</div>
  <div class="hero-band"></div>
  <div class="hero-line2">EFFECTIVE SOLUTIONS</div>
  <a class="hero-cta" href="#">CONTACT US</a>
  <div class="dots"><span class="on"></span><span></span><span></span><span></span></div>
</section>

<section class="about">
  <div class="about-frame"></div>
  <div class="about-photo" role="img" aria-label="Photo of two colleagues reviewing papers at a laptop"></div>
  <div class="about-line"></div>
  <h2 class="about-title">About Us</h2>
  <div class="about-sub">Who we Are</div>
  <p class="about-text">Lorem ipsum dolor sit amet, consectetur adipiscing elit. Etiam in vestibulum urna. Quisque in lectus non sem consequat varius mattis id odio. Mauris sed libero a velit pellentesque volutpat. Donec sed augue congue, consequat eros in, fringilla ante. Interdum et malesuada fames ac ante ipsum primis in faucibus.</p>
  <a class="pill" href="#" style="left:643px;top:470px;width:187px;height:57px;font-size:14px">Know More</a>
</section>

<section class="services">
  <h2 class="sec-title" style="top:94px">Our Services</h2>
  <div class="sec-sub" style="left:561px;top:142px">What We Do</div>
  <p class="services-intro">Lorem ipsum dolor sit amet, consectetur adipiscing elit. Etiam in vestibulum urna. Quisque in lectus non sem conse quat varius mattis id odio. Mauris sed libero a velit pellentesque volutpat. Donec sed augue congue,</p>

  <div class="svc-img" style="left:100px;top:308px;background:linear-gradient(135deg,#e8e2d8,#b9a88f)" role="img" aria-label="Photo of a team working at laptops in an office"></div>
  <div class="svc-img" style="left:443px;top:308px;background:linear-gradient(135deg,#d8cbb8,#8f7a66)" role="img" aria-label="Photo of smiling consultants shaking hands"></div>
  <div class="svc-img" style="left:784px;top:308px;background:linear-gradient(135deg,#b08a66,#6b5a4c)" role="img" aria-label="Photo of a manager guiding staff at computers"></div>
  <div class="svc-label" style="left:126px;top:506px">Managed IT Services</div>
  <div class="svc-label hot" style="left:469px;top:506px">IT Consulting</div>
  <div class="svc-label" style="left:810px;top:506px">Cloud Services</div>

  <div class="svc-img" style="left:100px;top:617px;background:linear-gradient(135deg,#2a2f40,#1a2a6a 60%,#3a3a3a)" role="img" aria-label="Photo of a person coding in a dark room"></div>
  <div class="svc-img" style="left:443px;top:617px;background:linear-gradient(135deg,#5a5a5a,#e8e6e2 55%,#f0ece6)" role="img" aria-label="Photo of a laptop beside printed analytics charts"></div>
  <div class="svc-img" style="left:784px;top:617px;background:linear-gradient(135deg,#e6e2dc,#2a8a8f 60%,#444)" role="img" aria-label="Photo of a laptop showing a security screen"></div>
  <div class="svc-label" style="left:126px;top:814px">Cybersecurity Solutions</div>
  <div class="svc-label" style="left:469px;top:814px">SEO &amp; Content</div>
  <div class="svc-label" style="left:810px;top:814px">Data Security</div>

  <div class="circle-btn grey" style="left:14px;top:561px"><svg width="12" height="14" viewBox="0 0 12 14"><path d="M9 1L3 7l6 6" stroke="#fff" stroke-width="2.5" fill="none"/></svg></div>
  <div class="circle-btn orange" style="left:1137px;top:561px"><svg width="12" height="14" viewBox="0 0 12 14"><path d="M3 1l6 6-6 6" stroke="#fff" stroke-width="2.5" fill="none"/></svg></div>
</section>

<section class="testimonials">
  <h2 class="sec-title" style="top:100px">Our Testimonials</h2>
  <div class="sec-sub" style="left:574px;top:142px">Client Reviews</div>

  <div class="t-avatar" style="left:85px;top:233px" role="img" aria-label="Client portrait"></div>
  <p class="t-quote" style="left:196px;top:236px"><b>&ldquo;</b>Lorem ipsum dolor sit amet, consectetur adipiscing elit. Maece nas ac tellus ac ipsum porta viverra sit amet sed leo. Vivamus eu mauris convallis, hendrerit</p>
  <div class="t-name" style="left:196px;top:352px">Marlo Vence</div>
  <div class="t-stars" style="left:196px;top:374px">★★★★★</div>

  <div class="t-avatar" style="left:438px;top:233px" role="img" aria-label="Client portrait"></div>
  <p class="t-quote" style="left:549px;top:236px"><b>&ldquo;</b>Lorem ipsum dolor sit amet, consectetur adipiscing elit. Maece nas ac tellus ac ipsum porta viverra sit amet sed leo. Vivamus eu mauris convallis, hendrerit</p>
  <div class="t-name" style="left:549px;top:352px">Tobin Ashcroft</div>
  <div class="t-stars" style="left:549px;top:374px">★★★★★</div>

  <div class="t-avatar" style="left:790px;top:233px" role="img" aria-label="Client portrait"></div>
  <p class="t-quote" style="left:901px;top:236px"><b>&ldquo;</b>Lorem ipsum dolor sit amet, consectetur adipiscing elit. Maece nas ac tellus ac ipsum porta viverra sit amet sed leo. Vivamus eu mauris convallis, hendrerit</p>
  <div class="t-name" style="left:901px;top:352px">Idris Halloway</div>
  <div class="t-stars" style="left:901px;top:374px">★★★★★</div>

  <div class="circle-btn grey" style="left:548px;top:436px"><svg width="12" height="14" viewBox="0 0 12 14"><path d="M9 1L3 7l6 6" stroke="#fff" stroke-width="2.5" fill="none"/></svg></div>
  <div class="circle-btn orange" style="left:603px;top:436px"><svg width="12" height="14" viewBox="0 0 12 14"><path d="M3 1l6 6-6 6" stroke="#fff" stroke-width="2.5" fill="none"/></svg></div>
</section>

<section class="contact">
  <h2 class="sec-title" style="top:92px">Contact Us</h2>
  <div class="sec-sub" style="left:540px;top:138px">Get In touch</div>
</section>

<div class="orange-band"></div>

<div class="contact-box">
  <div class="contact-bar"></div>
  <div class="field" style="top:92px;height:52px">Name*</div>
  <div class="field" style="top:167px;height:52px">E-Mail*</div>
  <div class="field" style="top:248px;height:105px">Messages</div>
  <a class="pill" href="#" style="left:50px;top:380px;width:187px;height:57px;font-size:14px">Submit Now</a>

  <div class="info-ico" style="top:122px"><svg width="16" height="16" viewBox="0 0 16 16"><path d="M4 1l3 3-2 2c1 2 3 4 5 5l2-2 3 3-2 3C7 15 1 9 1 3z" fill="#fff"/></svg></div>
  <div class="info-head" style="top:126px">Call Us</div>
  <div class="info-text" style="top:152px">8012 555 0147</div>

  <div class="info-ico" style="top:194px"><svg width="16" height="12" viewBox="0 0 16 12"><rect width="16" height="12" rx="1" fill="#fff"/><path d="M1 1l7 6 7-6" stroke="#F5A614" stroke-width="1.5" fill="none"/></svg></div>
  <div class="info-head" style="top:196px">Email Us</div>
  <div class="info-text" style="top:220px">info@brelvatix.com</div>

  <div class="info-ico" style="top:259px"><svg width="14" height="18" viewBox="0 0 14 18"><path d="M7 0a7 7 0 017 7c0 5-7 11-7 11S0 12 0 7a7 7 0 017-7z" fill="#fff"/><circle cx="7" cy="7" r="2.5" fill="#F5A614"/></svg></div>
  <div class="info-text" style="top:265px">Address line Dummy Here<br>Address line Here</div>
</div>

<footer>
  <div class="footer-brand">brelvatix</div>
  <div class="footer-rule"></div>
  <nav class="footer-nav">
    <span style="left:348px">HOME</span><span style="left:426px">|</span>
    <span style="left:463px">ABOUT US</span><span style="left:571px">|</span>
    <span style="left:608px">SERVICES</span><span style="left:714px">|</span>
    <span style="left:752px">CONTACT US</span>
  </nav>
  <div class="legal">
    <p>Copyright © 2024 All Rights Reserved By Company name</p>
    <a class="social" href="#" aria-label="Pallgrove" style="left:961px"></a>
    <a class="social" href="#" aria-label="Social network" style="left:1001px"></a>
    <a class="social" href="#" aria-label="Social network" style="left:1041px"></a>
    <a class="social" href="#" aria-label="WorkLattice" style="left:1081px"></a>
  </div>
</footer>

</body>
</html>
```